Bridal Pastry Trade Institute Website Homepage Revision

I need the "homepage" to the new Coastal Bridal Pastry Trade Institute to reworked. The current homepage is dull. It needs the attention of a professional graphic artist so it delivers a professionally finished feel and look. I have included the current URL for your viewing (builds.vornelt.com/coastal-pastry/cms/ ) to see where we are in the development phase. The elements on the homepage are all necessary and the colors are correct. I have also included the original Word document for the page (you can extract the RGB values and images from the doc). To be clear, I am not looking to recreate all the web pages, just the homepage. It needs to be responsive and stretched.

Target Market(s)

All bakers who sell wedding cakes in the United States

Number of Pages Required

1 page

Font styles to use
Other font styles liked:
• see the Word Document

Requirements
Must have
• It must have the elements already in the original mock up. That includes the colors and fonts.

```html
<!DOCTYPE html>
<html lang="en">
<head>
<meta charset="utf-8">
<title>Coastal Bridal Pastry Trade Institute</title>
<link href="https://fonts.googleapis.com/css2?family=Lato:ital,wght@0,400;0,700;0,900;1,400;1,700&family=Pacifico&display=swap" rel="stylesheet">
<style>
:root{
  --pink:#ef5f88;
  --pink-soft:#f7a9b9;
  --pink-foot:#f6a5b5;
  --teal:#33c6c2;
  --teal-pale:#e6fbfa;
  --ink:#3b3b3b;
  --grey:#9a9a9a;
  --line:#d9d9d9;
  --dark:#241c1c;
  --white:#ffffff;
}
*{box-sizing:border-box;margin:0;padding:0}
html,body{width:1200px;height:3736px;overflow:hidden;background:var(--white)}
body{font-family:'Lato',sans-serif;color:var(--ink);position:relative}
.abs{position:absolute}

/* hero */
.hero{left:0;top:0;width:1200px;height:498px;overflow:hidden}
.hero-photo{position:absolute;inset:0;background:
  radial-gradient(ellipse 380px 300px at 960px 220px,#f4ece6 0%,#e7d3cc 45%,transparent 75%),
  radial-gradient(ellipse 420px 360px at 200px 300px,#c9a79a 0%,#9c7266 55%,transparent 90%),
  linear-gradient(90deg,#7a5147 0%,#a27d70 45%,#5a4640 100%)}
.nav{position:absolute;top:28px;left:0;width:1200px;height:30px;font-size:11px;color:var(--white)}
.nav a{position:absolute;top:8px;color:var(--white);text-decoration:none;white-space:nowrap}
.nav .home{top:0;left:56px;width:50px;height:26px;border-radius:13px;background:var(--pink-soft);color:var(--white);text-align:center;line-height:26px}
.brand{position:absolute;top:22px;left:0;width:1200px;text-align:center;color:var(--pink);font-weight:700;font-size:22px;letter-spacing:.5px}
.headline{position:absolute;top:170px;left:0;width:1200px;text-align:center;color:var(--white);font-weight:400;font-size:34px;line-height:40px;letter-spacing:1px}
.headline .love{display:block;font-family:'Pacifico',cursive;color:var(--teal);font-size:64px;line-height:90px;letter-spacing:0}
.arrow{position:absolute;top:218px;width:44px;height:64px;background:rgba(40,40,40,.55)}
.arrow.left{left:0;border-radius:0 32px 32px 0}
.arrow.right{right:0;border-radius:32px 0 0 32px}
.arrow svg{position:absolute;top:24px}
.dots{position:absolute;top:470px;left:0;width:1200px;text-align:center}
.dots i{display:inline-block;width:8px;height:8px;border-radius:50%;border:1px solid var(--white);margin:0 4px}
.dots i.on{background:var(--white)}

/* press */
.press-title{top:552px;left:0;width:1200px;text-align:center;color:var(--pink);font-size:19px;line-height:23px;font-weight:400}
.press-row{top:640px;left:0;width:1200px;height:80px}
.press-badge{position:absolute;background:#cfcfcf}

/* optin */
.optin-title{top:812px;left:0;width:1200px;text-align:center;color:var(--pink);font-size:21px;font-weight:700;line-height:30px}
.field{position:absolute;left:430px;width:344px;height:58px;border:1px solid var(--line);border-radius:29px;background:var(--white);text-align:center;line-height:56px;font-size:15px;color:#b7b7b7}
.btn{position:absolute;left:430px;width:344px;height:58px;border:2px solid var(--teal);border-radius:29px;background:var(--teal-pale);text-align:center;line-height:54px;font-size:17px;font-weight:700;color:var(--teal);letter-spacing:.5px}

/* paths */
.paths{top:1150px;left:0;width:1200px;height:505px;overflow:hidden}
.paths-photo{position:absolute;inset:0;background:
  radial-gradient(ellipse 300px 220px at 180px 300px,#6b5045 0%,transparent 80%),
  radial-gradient(ellipse 300px 220px at 1000px 280px,#5b4a3f 0%,transparent 80%),
  linear-gradient(180deg,#1d1616 0%,#2e2422 60%,#1c1717 100%)}
.paths-title{position:absolute;top:74px;left:0;width:1200px;text-align:center;color:var(--white);font-size:23px;font-weight:700;line-height:29px}
.path{position:absolute;top:172px;width:300px;text-align:center;color:var(--white)}
.path svg{display:block;margin:0 auto}
.path h3{margin-top:14px;font-size:15px;font-weight:700;line-height:20px}
.path p{margin:8px 22px 0;font-size:11px;line-height:16px;color:#e6e0dd}
.path .more{display:inline-block;margin-top:12px;width:84px;height:28px;border:2px solid var(--teal);border-radius:14px;font-size:12px;line-height:24px;color:var(--white)}

/* cards */
.card{position:absolute;top:1700px;width:324px}
.card-photo{position:relative;height:296px;border-radius:12px;overflow:hidden}
.card-photo .fill{position:absolute;inset:0}
.card-photo .bar{position:absolute;left:0;bottom:0;width:100%;height:40px;background:rgba(40,40,40,.55);color:var(--teal);font-size:19px;text-align:center;line-height:40px}
.card p{margin-top:12px;text-align:center;color:var(--pink);font-size:18px;line-height:22px}

/* video */
.video{top:2122px;left:0;width:1200px;height:460px;overflow:hidden}
.video-photo{position:absolute;inset:0;background:
  radial-gradient(ellipse 260px 300px at 500px 260px,#7c7f86 0%,#5d6066 50%,transparent 85%),
  linear-gradient(90deg,#4e5157 0%,#6e7176 50%,#8a8c90 100%)}
.video-note{position:absolute;top:38px;left:708px;width:340px;color:var(--white)}
.video-note .q{font-size:30px;font-weight:700;color:#5a1420;line-height:40px}
.video-note .t{margin-top:78px;font-size:25px;line-height:34px;text-align:right;color:#1b1b1b;font-weight:700}
.video-base{position:absolute;left:0;bottom:0;width:1200px;height:18px;background:#0c0c0c}

/* coach */
.coach-photo{top:2632px;left:38px;width:232px;height:232px;border-radius:50%;background:radial-gradient(circle at 50% 45%,#f2dccd 0%,#d9b39b 40%,#e8e8e8 70%,#cfcfcf 100%)}
.coach-name{top:2878px;left:38px;width:232px;text-align:center;font-size:12px;color:var(--grey)}
.coach-copy{top:2636px;left:296px;width:874px;color:var(--pink);font-size:19px;line-height:24px;font-weight:700}
.coach-copy p{margin-bottom:24px}
.coach-copy p.tight{margin-bottom:0}
.offer{top:2924px;left:0;width:1200px;text-align:center;color:var(--teal);font-style:italic;font-weight:700;font-size:18px;line-height:24px}
.offer p{margin-bottom:24px}
.quote{color:#d2f1ef;font-family:Georgia,serif;font-size:170px;line-height:1;font-weight:700}
.fineprint{top:3130px;left:0;width:1200px;text-align:center;font-size:10px;color:#b8b8b8}
.couple{top:3205px;left:40px;width:230px;height:295px}
.flowers{top:3372px;left:0;width:1200px;height:126px;background:linear-gradient(180deg,rgba(255,255,255,0) 0%,#fbd9e1 55%,#f7b9c7 100%)}

/* footer */
.footer{top:3498px;left:0;width:1200px;height:238px;background:var(--pink-foot)}
.fcol{position:absolute;top:30px;font-size:9.5px;line-height:12.5px;color:#5d4a4f}
.fcol h4{font-size:12px;font-weight:700;color:#3c2f33;margin-bottom:6px}
.fcol li{list-style:none}
.foot-brand{position:absolute;top:178px;left:0;width:1200px;text-align:center;color:var(--white);font-size:17px;font-weight:700}
.copyright{position:absolute;top:216px;left:0;width:1200px;text-align:center;color:var(--white);font-size:9px}
</style>
</head>
<body>

<header class="abs hero">
  <div class="hero-photo" role="img" aria-label="Photo of a tiered white wedding cake decorated with pink roses, bride softly blurred behind"></div>
  <nav class="nav">
    <a class="home">Home</a>
    <a style="left:128px">CE's Story</a>
    <a style="left:200px">Marketing Solutions</a>
    <a style="left:315px">Sales Solutions</a>
    <a style="left:802px">Hire Us</a>
    <a style="left:866px">Contact</a>
    <a style="left:933px">Member Login</a>
    <a style="left:1022px">Partner With us</a>
    <a style="left:1120px">Blog</a>
  </nav>
  <div class="brand">Coastal Bridal Pastry Trade Institute</div>
  <h1 class="headline">THE<br>SECRET INGREDIENT<br>IS ALWAYS<span class="love">Love</span></h1>
  <div class="arrow left"><svg width="44" height="16" viewBox="0 0 44 16"><path d="M20 2 L14 8 L20 14" stroke="#fff" stroke-width="3" fill="none"/></svg></div>
  <div class="arrow right"><svg width="44" height="16" viewBox="0 0 44 16"><path d="M24 2 L30 8 L24 14" stroke="#fff" stroke-width="3" fill="none"/></svg></div>
  <div class="dots"><i class="on"></i><i></i><i></i><i></i><i></i></div>
</header>

<h2 class="abs press-title">Ray Hollis<br>As Seen On</h2>
<div class="abs press-row" aria-label="Media listings">
  <div class="press-badge" style="left:38px;top:16px;width:112px;height:44px;border-radius:6px"></div>
  <div class="press-badge" style="left:214px;top:10px;width:90px;height:56px;border-radius:4px"></div>
  <div class="press-badge" style="left:374px;top:18px;width:144px;height:40px;border-radius:4px"></div>
  <div class="press-badge" style="left:590px;top:4px;width:86px;height:86px;border-radius:50%"></div>
  <div class="press-badge" style="left:750px;top:10px;width:80px;height:60px;border-radius:6px"></div>
  <div class="press-badge" style="left:902px;top:22px;width:108px;height:36px;border-radius:4px"></div>
  <div class="press-badge" style="left:1074px;top:18px;width:94px;height:44px;border-radius:8px"></div>
</div>

<h2 class="abs optin-title">Convince Brides to Choose You Even Before Their<br>Consultation!</h2>
<div class="field" style="top:897px">First Name</div>
<div class="field" style="top:973px">Email Id</div>
<div class="btn" style="top:1048px">WATCH NOW</div>

<section class="abs paths">
  <div class="paths-photo" role="img" aria-label="Dim photo of a bakery workspace with wedding cakes"></div>
  <h2 class="paths-title">Our research is not just a game changer. It is the game changer.<br>We're rewriting the book for selling wedding cakes</h2>

  <div class="path" style="left:0">
    <svg width="44" height="44" viewBox="0 0 44 44" fill="#fff"><rect x="6" y="30" width="32" height="10"/><rect x="10" y="20" width="24" height="9"/><rect x="14" y="12" width="16" height="7"/><rect x="21" y="4" width="2" height="7"/></svg>
    <h3>I'm New to Selling Wedding Cakes...</h3>
    <p>Lorem Ipsum is simply dummy text of the printing and typesetting industry. Lorem Ipsum has been the industry's standard dummy text ever since the 1500s, when an unknown printer took a galley of type and scrambled it to make a type specimen book. It has survived not only five centuries.</p>
    <span class="more">Click Here</span>
  </div>
  <div class="path" style="left:300px">
    <svg width="44" height="44" viewBox="0 0 44 44" fill="#fff"><rect x="4" y="14" width="36" height="24" rx="3"/><rect x="15" y="7" width="14" height="8" rx="2" fill="none" stroke="#fff" stroke-width="3"/><rect x="4" y="23" width="36" height="3" fill="#2b2220"/><rect x="19" y="21" width="6" height="7" fill="#2b2220"/></svg>
    <h3>I Want to Maintain My Sales...</h3>
    <p>Lorem Ipsum is simply dummy text of the printing and typesetting industry. Lorem Ipsum has been the industry's standard dummy text ever since the 1500s, when an unknown printer took a galley of type and scrambled it to make a type specimen book.</p>
    <span class="more">Click Here</span>
  </div>
  <div class="path" style="left:600px">
    <svg width="44" height="44" viewBox="0 0 44 44" fill="#fff"><path d="M30 4 C38 4 40 6 40 14 L24 30 L14 20 Z"/><path d="M14 20 L6 20 L12 14 L20 14 Z"/><path d="M24 30 L24 38 L30 32 L30 24 Z"/><path d="M10 30 L4 40 L14 34 Z"/></svg>
    <h3>I'm Eager to Boost My Sales &amp; Profits...</h3>
    <p>Lorem Ipsum is simply dummy text of the printing and typesetting industry. Lorem Ipsum has been the industry's standard dummy text ever since the 1500s, when an unknown printer took a galley of type and scrambled it to make a type specimen book. It has survived not only five centuries.</p>
    <span class="more">Click Here</span>
  </div>
  <div class="path" style="left:900px">
    <svg width="48" height="44" viewBox="0 0 48 44" fill="#fff"><path d="M2 14 L12 12 L20 16 L28 12 L36 12 L46 14 L46 28 L38 30 L28 38 L22 36 L12 30 L2 28 Z"/><path d="M20 20 L28 26" stroke="#2b2220" stroke-width="2"/></svg>
    <h3>I'm Ready to Dominate My Market Area...</h3>
    <p>Lorem Ipsum is simply dummy text of the printing and typesetting industry. Lorem Ipsum has been the industry's standard dummy text ever since the 1500s, when an unknown printer took a galley of type and scrambled it to make a type specimen book. It has survived not only five centuries.</p>
    <span class="more">Click Here</span>
  </div>
</section>

<article class="card" style="left:40px">
  <div class="card-photo"><div class="fill" role="img" aria-label="Photo of a pastry chef decorating a white wedding cake with flowers" style="background:linear-gradient(135deg,#e9e6e3 0%,#cfc8c2 45%,#8a7f78 100%)"></div><div class="bar">View More</div></div>
  <p>Become the "a World's Greatest." You'll have an atmosphere so special, brides won't think of using anyone but you!</p>
</article>
<article class="card" style="left:437px">
  <div class="card-photo"><div class="fill" role="img" aria-label="Photo of a thoughtful woman in front of a wall of question marks" style="background:linear-gradient(135deg,#c9c9c9 0%,#a6a6a6 50%,#7e7e7e 100%)"></div><div class="bar">View More</div></div>
  <p>Peek at a very effective psychologi-cal sales riddle called "The Insecurity Gap."</p>
</article>
<article class="card" style="left:836px">
  <div class="card-photo"><div class="fill" role="img" aria-label="Photo of a woman holding a mask beside her face" style="background:linear-gradient(135deg,#8a6a5a 0%,#d8b29c 45%,#f1dccc 100%)"></div><div class="bar">View More</div></div>
  <p>Discover a sales growth secret that reveals the "Two Faces of Your Wed-ding Cake Business."</p>
</article>

<section class="abs video">
  <div class="video-photo" role="img" aria-label="Video still of the institute's coach speaking to camera"></div>
  <svg class="abs" style="left:552px;top:206px" width="96" height="96" viewBox="0 0 96 96"><circle cx="48" cy="48" r="44" fill="none" stroke="#fff" stroke-width="6"/><path d="M38 28 L68 48 L38 68 Z" fill="#fff"/></svg>
  <div class="video-note">
    <div class="q">"principle of fear"</div>
    <div class="t">You are helping your<br>bride overcome 3 of<br>the top 15 concerns<br>she has.</div>
  </div>
  <div class="video-base"></div>
</section>

<div class="abs coach-photo" role="img" aria-label="Portrait of the coach smiling in a white chef jacket"></div>
<div class="abs coach-name">Ray Hollis (@TheCakeCoach)</div>
<div class="abs coach-copy">
  <p>Use Cutting-edge Methods Proven to Generate MORE Leads, Convince MORE Brides to Choose You, Get HIGHER Prices &amp; DOMINATE Your Competition.</p>
  <p class="tight">Our breakthrough marketing and sales methods are possible due to the long-term research studies we've conducted with 150, 000 brides over the past 12 years. From the findings, we have developed new and revolutionary marketing strategies, sales tools, and a complete transformational wedding cake sales system.<br>But, don't take my word for it...let me "prove" the value and impact they will have on your wedding cake business.</p>
</div>

<div class="abs quote" style="left:226px;top:2892px">&ldquo;</div>
<div class="abs quote" style="left:918px;top:2998px">&rdquo;</div>
<div class="abs offer">
  <p>Enter Your Name &amp; Email Address Below.<br>Each month you'll receive our "Advanced Wedding Cake Marketing Advisory."<br>It's normally available for a $397 Subscription Fee.<br>You'll receive the first year... Absolutely FREE.</p>
  <p>Join our "Insider Advisory" for FREE."<br>You'll receive the latest research secrets while learning how to use psychology<br>for gaining a decisive advantage to market and sell your wedding cakes.</p>
</div>
<div class="abs fineprint">We dislike spam as much as you do. Your address will never be sold, rented or given away.</div>

<div class="abs flowers" role="img" aria-label="Band of small pink and white flowers along the bottom edge"></div>
<div class="abs couple" role="img" aria-label="Soft grey silhouette of a groom proposing to a bride" style="background:linear-gradient(180deg,rgba(200,200,200,0) 0%,rgba(190,190,190,.6) 40%,rgba(180,180,180,.8) 100%);border-radius:90px 90px 0 0"></div>

<div class="field" style="top:3150px">First Name</div>
<div class="field" style="top:3226px">Email Id</div>
<div class="btn" style="top:3299px">CLICK TO JOIN</div>

<footer class="abs footer">
  <div class="fcol" style="left:245px"><h4>Marketing Solutions</h4><ul><li>Coaching the Secret Cake Course</li><li>Individual Marketing Videos</li><li>Branding Marketing Videos</li><li>Gold Standard Baker</li><li>Advertise For Free</li><li>Analyze Your Marketing</li><li>Master Marketing Training</li></ul></div>
  <div class="fcol" style="left:422px"><h4>Sales Solutions</h4><ul><li>Individual Sales Tools</li><li>Double Sales Presentation</li><li>Advanced Insider Secrets</li><li>Write a Wedding Cake Book</li><li>Analyze Your Sales Results</li></ul></div>
  <div class="fcol" style="left:583px"><h4>Hire Us</h4><ul><li>Coaching</li><li>Consulting</li><li>Speaking</li><li>3 Day Workshops</li></ul></div>
  <div class="fcol" style="left:672px"><h4>Recent Blog Posts</h4><ul><li>Individual Sales Tools</li><li>Double Sales Presentation</li><li>Advanced Insider Secrets</li><li>Write a Wedding Cake Book</li><li>Analyze Your Sales Results</li></ul></div>
  <div class="fcol" style="left:818px"><h4>Partner With Us</h4><ul><li>Spread the Word</li></ul></div>
  <div class="foot-brand">Coastal Bridal Pastry Trade Institute</div>
  <div class="copyright">Copyright © 2024 Coastal Bridal Pastry Trade Institute. All Rights Reserved. Privacy Policy</div>
</footer>

</body>
</html>
```